BUSINESS CARD MIRELLE CAVANOSI

I need a new business card for my personal business.
I am a Naturopath and Nutritionist working doing private consults in the health and wellness arena.
I would like to see designs that are, clean minimalist but colourful.
I like:
White (clean,fresh, minimalist)
pops of one colour ONLY.Choose a colour to run with and keep it simple.
green
light blue
mustard
Bright yellow
Charcoal
The final design should communicate professionalism but also be in touch with nature.
Key Information to include:
MIRELLE CAVANOSI
ABN 48 217 603 915
RQTLBE 327081
Tel 0487 639 142
NATUROPATH | HERBALIST | NUTRITON CONSULTANT
BHSc (Naturopathic Studies) Grad Dip (Naturopathy)
BACK OF CARD : YOUR NEXT APPOINTMENT ..................................
I already have a logo (picture attached)But I would be more than happy to NOT have this included. I am very Open to cards WITHOUT current logo/ ones that weave the colour of my logo but do not use the logo.
I have included pictures attached to give examples of the styles/colors I enjoy.
Updates
I have added a picture of a mortar and pestle - one just like this would be lovely to include in your entry.
TIA

```html
<!DOCTYPE html>
<html lang="en">
<head>
<meta charset="utf-8">
<title>Mirelle Cavanosi — Business Card</title>
<link href="https://fonts.googleapis.com/css2?family=Arimo:wght@400;500&display=swap" rel="stylesheet">
<style>
  :root {
    --page: #e9e9e6;
    --card: #ffffff;
    --leaf-pale: #eef1e6;
    --leaf-mid: #e3e7d8;
    --lime: #c5d82a;
    --ink: #1e1e1e;
    --ink-soft: #2b2b2b;
  }
  * { box-sizing: border-box; margin: 0; padding: 0; }
  html, body {
    width: 1200px; height: 1000px; overflow: hidden;
    background: var(--page);
    font-family: "Arimo", Arial, sans-serif;
    color: var(--ink);
  }
  .sheet {
    width: 1200px; height: 1000px;
    display: flex; flex-direction: column; align-items: center; justify-content: center;
    gap: 32px;
  }
  .card {
    position: relative;
    width: 740px; height: 452px;
    background: var(--card);
    overflow: hidden;
    box-shadow: 0 6px 18px rgba(0,0,0,0.12);
  }
  .leaf-field {
    position: absolute; inset: 0;
    background:
      radial-gradient(ellipse at 20% 30%, var(--leaf-mid), transparent 60%),
      radial-gradient(ellipse at 75% 70%, var(--leaf-mid), transparent 55%),
      var(--leaf-pale);
  }
  .card--front .leaf-field { opacity: 0.45; }

  /* Front */
  .identity {
    position: absolute; left: 250px; top: 48px; right: 30px;
  }
  .identity__name {
    font-size: 58px; font-weight: 400; letter-spacing: 1px; line-height: 1;
    color: var(--ink);
  }
  .identity__role,
  .identity__quals {
    font-size: 15px; line-height: 1.35; color: var(--ink-soft);
    margin-left: 4px;
  }
  .identity__role { margin-top: 10px; }

  .details-band {
    position: absolute; left: 0; right: 0; top: 240px; height: 110px;
    background: var(--lime);
    display: flex; align-items: center; justify-content: space-between;
    padding: 0 36px;
    font-size: 16px; color: var(--ink);
  }
  .details-band__divider { width: 40px; height: 60px; }

  /* Back */
  .appointment-band {
    position: absolute; left: 0; right: 0; top: 170px; height: 112px;
    background: var(--lime);
    display: flex; align-items: center;
    padding-left: 44px;
  }
  .appointment-band__label {
    font-size: 38px; font-weight: 400; letter-spacing: 0.5px; color: var(--ink);
  }
</style>
</head>
<body>
<main class="sheet">
  <section class="card card--front" aria-label="Card front">
    <div class="leaf-field" role="img" aria-label="Faint pattern of pale leaves"></div>
    <div class="identity">
      <h1 class="identity__name">MIRELLE CAVANOSI</h1>
      <p class="identity__role">NATUROPATH | HERBALIST | NUTRITON CONSULTANT</p>
      <p class="identity__quals">BHSc (Naturopathic Studies) Grad Dip (Naturopathy)</p>
    </div>
    <div class="details-band">
      <span class="details-band__item">ABN 48 217 603 915</span>
      <svg class="details-band__divider" viewBox="0 0 40 60" aria-hidden="true"><line x1="30" y1="4" x2="10" y2="56" stroke="#1e1e1e" stroke-width="2.5"/></svg>
      <span class="details-band__item">RQTLBE 327081</span>
      <svg class="details-band__divider" viewBox="0 0 40 60" aria-hidden="true"><line x1="30" y1="4" x2="10" y2="56" stroke="#1e1e1e" stroke-width="2.5"/></svg>
      <span class="details-band__item">Tel 0487 639 142</span>
    </div>
  </section>

  <section class="card card--back" aria-label="Card back">
    <div class="leaf-field" role="img" aria-label="Pattern of pale green and grey leaves"></div>
    <div class="appointment-band">
      <p class="appointment-band__label">YOUR NEXT APPOINTMENT ...</p>
    </div>
  </section>
</main>
</body>
</html>
```